Customer Appreciation Event

We (Harlow Provisions, a chain of butcher shops) are releasing a physical mailer (6x12 poster size) for a customer appreciation event we are doing at our Thornbury Ridge location in Vancouver, BC. These mailers will be dropped at potential client's houses to encourage them to come to our event.
The event will be on June 24, 2023, from 11am to 6pm. A few things that need to be included in the mailer:
-Address is 3172 Ellery St, Vancouver, BC, V5R 1K8
-We will be having a Hot Dog BBQ, In-Store Sampling, Gift Card and Product Raffles, and the entire store will be 10% off
I have attached our company logos below.

```html
<!DOCTYPE html>
<html lang="en">
<head>
<meta charset="utf-8">
<title>Harlow Provisions – Customer Appreciation Event</title>
<link rel="stylesheet" href="https://fonts.googleapis.com/css2?family=Montserrat:wght@500;600;800&family=Kaushan+Script&display=swap">
<style>
  :root {
    --page-bg: #e7e7e7;
    --wood-dark: #2a2725;
    --wood-mid: #3b3734;
    --accent-yellow: #ffcc00;
    --text-light: #ffffff;
    --text-dark: #1f1d1b;
    --offer-red: #d8141f;
    --offer-orange: #f7a21b;
  }
  * { box-sizing: border-box; margin: 0; padding: 0; }
  html, body {
    width: 891px;
    height: 1200px;
    overflow: hidden;
    background: var(--page-bg);
  }
  .mailer {
    position: absolute;
    left: 145px;
    top: 0;
    width: 600px;
    height: 1200px;
    overflow: hidden;
    background: linear-gradient(90deg, var(--wood-dark), var(--wood-mid) 35%, var(--wood-dark) 60%, var(--wood-mid) 85%, var(--wood-dark));
    font-family: "Montserrat", sans-serif;
  }
  .artwork { position: absolute; inset: 0; }
  .brand-name {
    position: absolute;
    top: 50px;
    left: 0;
    width: 100%;
    text-align: center;
    color: var(--text-light);
    font-family: "Montserrat", sans-serif;
    font-weight: 600;
    font-size: 30px;
    letter-spacing: 3px;
    text-transform: uppercase;
  }
  .tagline {
    position: absolute;
    top: 158px;
    left: 100px;
    width: 400px;
    text-align: center;
    font-family: "Kaushan Script", cursive;
    font-size: 46px;
    line-height: 52px;
    color: var(--text-light);
  }
  .tagline .hl { color: var(--accent-yellow); }
  .event-details {
    position: absolute;
    top: 772px;
    left: 40px;
    width: 520px;
    text-align: center;
  }
  .intro {
    color: var(--text-light);
    font-weight: 500;
    font-size: 20px;
    line-height: 28px;
  }
  .activities {
    color: var(--accent-yellow);
    font-weight: 800;
    font-size: 20.5px;
    line-height: 30px;
  }
  .divider {
    width: 278px;
    height: 2px;
    background: var(--text-light);
    margin: 12px auto 14px;
  }
  .when-label {
    color: var(--text-light);
    font-weight: 500;
    font-size: 16px;
  }
  .when {
    margin-top: 8px;
    display: flex;
    justify-content: center;
    align-items: center;
    gap: 10px;
    color: var(--accent-yellow);
    font-weight: 800;
    font-size: 21px;
  }
  .when svg { flex: none; }
  .when .time { margin-left: 6px; }
  .location {
    position: absolute;
    top: 1100px;
    left: 0;
    width: 100%;
    text-align: center;
    color: var(--text-dark);
    font-weight: 500;
    font-size: 18px;
    line-height: 21px;
  }
  .social-dots {
    position: absolute;
    top: 1161px;
    left: 0;
    width: 100%;
    display: flex;
    justify-content: center;
    gap: 5px;
  }
  .social-dots span {
    width: 16px;
    height: 16px;
    border-radius: 50%;
    background: var(--text-dark);
  }
</style>
</head>
<body>
<main class="mailer">
  <svg class="artwork" width="600" height="1200" viewBox="0 0 600 1200" xmlns="http://www.w3.org/2000/svg">
    <defs>
      <linearGradient id="spiceTone" x1="0" y1="0" x2="1" y2="1">
        <stop offset="0" stop-color="#8a3a1c"/>
        <stop offset="0.5" stop-color="#5a3422" stop-opacity="0.8"/>
        <stop offset="1" stop-color="#2a2725" stop-opacity="0"/>
      </linearGradient>
      <linearGradient id="grillSceneTone" x1="0" y1="0" x2="0" y2="1">
        <stop offset="0" stop-color="#c9a24a"/>
        <stop offset="0.45" stop-color="#7d8d86"/>
        <stop offset="1" stop-color="#4a3c34"/>
      </linearGradient>
      <linearGradient id="platterTone" x1="0" y1="0" x2="1" y2="1">
        <stop offset="0" stop-color="#9b3a2a"/>
        <stop offset="0.5" stop-color="#6a3a26"/>
        <stop offset="1" stop-color="#b06a3a"/>
      </linearGradient>
      <linearGradient id="hotdogTone" x1="0" y1="0" x2="1" y2="1">
        <stop offset="0" stop-color="#6f9a3a"/>
        <stop offset="0.5" stop-color="#c98a4a"/>
        <stop offset="1" stop-color="#a24a2c"/>
      </linearGradient>
      <linearGradient id="burgerTone" x1="0" y1="0" x2="0" y2="1">
        <stop offset="0" stop-color="#3a2a1e"/>
        <stop offset="0.4" stop-color="#d8953e"/>
        <stop offset="0.7" stop-color="#6b3a22"/>
        <stop offset="1" stop-color="#c98a3e"/>
      </linearGradient>
      <linearGradient id="grillTone" x1="0" y1="0" x2="0" y2="1">
        <stop offset="0" stop-color="#2a2725" stop-opacity="0"/>
        <stop offset="0.25" stop-color="#3a2620"/>
        <stop offset="1" stop-color="#b3401a"/>
      </linearGradient>
      <radialGradient id="flameTone">
        <stop offset="0" stop-color="#ff7a1a" stop-opacity="0.9"/>
        <stop offset="1" stop-color="#ff7a1a" stop-opacity="0"/>
      </radialGradient>
      <linearGradient id="badgeTone" x1="0" y1="0" x2="1" y2="1">
        <stop offset="0" stop-color="#ffe033"/>
        <stop offset="1" stop-color="var(--offer-orange)"/>
      </linearGradient>
    </defs>

    <g role="img" aria-label="Photo of spices, chillies and wooden spoons on dark stone">
      <path d="M0 0 H120 C110 120 130 250 90 340 C60 380 20 410 0 420 Z" fill="url(#spiceTone)"/>
    </g>

    <g role="img" aria-label="Photo of the fire glowing beneath a barbecue grill grate, with flames at the sides">
      <rect x="0" y="980" width="600" height="220" fill="url(#grillTone)"/>
      <ellipse cx="20" cy="960" rx="60" ry="90" fill="url(#flameTone)"/>
      <ellipse cx="585" cy="960" rx="55" ry="90" fill="url(#flameTone)"/>
    </g>

    <g role="img" aria-label="Photo of a hand turning sausages on an outdoor grill">
      <polygon points="600,92 355,332 600,640" fill="url(#grillSceneTone)" stroke="#fff" stroke-width="4" stroke-linejoin="round"/>
    </g>

    <line x1="466" y1="604" x2="600" y2="759" stroke="#fff" stroke-width="3"/>
    <line x1="435" y1="631" x2="600" y2="828" stroke="var(--accent-yellow)" stroke-width="3"/>
    <line x1="401" y1="662" x2="600" y2="890" stroke="#fff" stroke-width="3"/>

    <g role="img" aria-label="Photo of a platter of grilled meats, peppers and tomatoes">
      <rect x="-116" y="-116" width="232" height="232" rx="26" transform="translate(354 535) rotate(45)" fill="url(#platterTone)" stroke="#fff" stroke-width="4"/>
    </g>
    <g role="img" aria-label="Photo of hot dogs with toppings and mustard">
      <rect x="-85" y="-85" width="170" height="170" rx="22" transform="translate(152 386) rotate(45)" fill="url(#hotdogTone)" stroke="#fff" stroke-width="4"/>
    </g>
    <g role="img" aria-label="Photo of a cheeseburger">
      <rect x="-82" y="-82" width="164" height="164" rx="22" transform="translate(159 555) rotate(45)" fill="url(#burgerTone)" stroke="#fff" stroke-width="4"/>
    </g>

    <g class="offer-badge">
      <circle cx="119" cy="714" r="48" fill="var(--offer-red)"/>
      <path d="M40 655 C40 620 90 605 140 615 C185 625 200 650 185 680 C170 705 110 710 70 700 C45 692 40 675 40 655 Z" fill="url(#badgeTone)"/>
      <circle cx="37" cy="714" r="5" fill="var(--accent-yellow)"/>
      <circle cx="58" cy="722" r="9" fill="var(--offer-red)"/>
      <text x="55" y="690" font-family="Montserrat, sans-serif" font-weight="800" font-size="50" fill="var(--offer-red)">10</text>
      <text x="120" y="664" font-family="Montserrat, sans-serif" font-weight="800" font-size="22" fill="#fff">%</text>
      <text x="121" y="688" font-family="Montserrat, sans-serif" font-weight="800" font-size="16" fill="#fff">OFF</text>
      <text x="119" y="724" text-anchor="middle" font-family="Montserrat, sans-serif" font-weight="500" font-size="13" fill="#fff">SPECIAL</text>
      <text x="119" y="742" text-anchor="middle" font-family="Montserrat, sans-serif" font-weight="800" font-size="16" fill="#fff">OFFER</text>
    </g>

    <path d="M0 1139 C120 1110 220 1062 300 1062 C380 1062 480 1110 600 1139 V1200 H0 Z" fill="var(--accent-yellow)"/>

    <g class="pin-icon" transform="translate(299 1056)">
      <path d="M0 26 C-10 12 -17 2 -17 -8 A17 17 0 0 1 17 -8 C17 2 10 12 0 26 Z" fill="#ec3f55"/>
      <circle cx="0" cy="-8" r="7" fill="#fff"/>
    </g>
  </svg>

  <div class="brand-name">Harlow Provisions</div>

  <h1 class="tagline">
    <span class="hl">Good</span> Food<br>
    Good <span class="hl">Mood</span>
  </h1>

  <section class="event-details">
    <p class="intro">We will be having a</p>
    <p class="activities">Hot Dog, BBQ,<br>In-Store Sampling, Gift Card and<br>Product Raffles</p>
    <div class="divider"></div>
    <p class="when-label">The event will be on:</p>
    <p class="when">
      <svg width="20" height="20" viewBox="0 0 20 20" aria-hidden="true">
        <rect x="2" y="4" width="16" height="14" rx="2" fill="none" stroke="#fff" stroke-width="1.6"/>
        <line x1="2" y1="8" x2="18" y2="8" stroke="#fff" stroke-width="1.6"/>
        <line x1="6" y1="2" x2="6" y2="5" stroke="#fff" stroke-width="1.6"/>
        <line x1="14" y1="2" x2="14" y2="5" stroke="#fff" stroke-width="1.6"/>
      </svg>
      <span>June 24, 2023</span>
      <svg class="time" width="20" height="20" viewBox="0 0 20 20" aria-hidden="true">
        <circle cx="10" cy="10" r="8" fill="none" stroke="#fff" stroke-width="1.6"/>
        <path d="M10 5 V10 L13 12" fill="none" stroke="#fff" stroke-width="1.6"/>
      </svg>
      <span>11am to 6pm.</span>
    </p>
  </section>

  <address class="location">3172 Ellery St,<br>Vancouver, BC, V5R 1K8</address>
  <div class="social-dots" aria-hidden="true"><span></span><span></span><span></span></div>
</main>
</body>
</html>
```